Business Card Design job - Tessa's Business Cards

Simple elegant feminine design - Going out on my own as a Mortgage Broker.
My thoughts are the following details on the Front, middle of the card possibly? Phone and email smaller font than my name?
Tessa Marwick
Finance Specialist
p: 0438 217 905
e: tessa@marwickfinance.com.au
Bottom of the card
residential / commercial / equipment
I would like the Font in Rose Gold maybe white or black background? or Possibly a stone grey - are you able to do a few options? I'd like them embossed
Then I had an idea as a simple logo as per the attached if you get the idea in my scribble, my initials, capital T attached to a small m that leads/follows into a circle? Thicker Font In Rose Gold, middle of the card at the back.
Very open to ideas though and what colour you think would look better with the Rose Gold.
Thanks so much for your help, I am not very creative and savvy with this stuff :-)
Industry/Entity Type
Finance
Contact Information for Business Card
Tessa Marwick
p: 0438 217 905
Look and feel
Each slider illustrates characteristics of the customer's brand and the style your logo design should communicate.

```html
<!DOCTYPE html>
<html lang="en">
<head>
<meta charset="utf-8">
<title>Tessa Marwick – Business Cards</title>
<link rel="stylesheet" href="https://fonts.googleapis.com/css2?family=Montserrat:wght@300;400&family=Permanent+Marker&display=swap">
<style>
  :root {
    --backdrop: #e9eaec;
    --card: #ffffff;
    --rose: #b56b74;
  }
  * { margin: 0; padding: 0; box-sizing: border-box; }
  html, body {
    width: 1200px;
    height: 1200px;
    overflow: hidden;
    background: var(--backdrop);
  }
  .canvas {
    position: relative;
    width: 1200px;
    height: 1200px;
  }
  .card {
    position: absolute;
    left: 246px;
    width: 700px;
    height: 400px;
    background: var(--card);
    color: var(--rose);
    font-family: "Montserrat", Arial, sans-serif;
    text-align: center;
  }
  .card--front { top: 146px; }
  .card--back { top: 652px; }

  .brand-mark {
    position: absolute;
    left: 50%;
    top: 84px;
    transform: translateX(-50%);
    display: flex;
    flex-direction: column;
    align-items: center;
    gap: 26px;
  }
  .brand-mark__circle {
    width: 160px;
    height: 160px;
    border-radius: 50%;
    background: var(--rose);
  }
  .brand-mark__name {
    font-size: 26px;
    font-weight: 400;
    letter-spacing: 4px;
    text-transform: uppercase;
    white-space: nowrap;
  }

  .contact-block {
    position: absolute;
    left: 0;
    right: 0;
    top: 100px;
  }
  .contact-block__name {
    font-family: "Permanent Marker", "Comic Sans MS", cursive;
    font-size: 36px;
    font-weight: 400;
    letter-spacing: 5px;
    line-height: 44px;
    text-transform: uppercase;
  }
  .contact-block__title {
    font-size: 23px;
    font-weight: 300;
    letter-spacing: 1px;
    line-height: 28px;
    text-transform: uppercase;
  }
  .contact-list {
    list-style: none;
    margin-top: 38px;
    font-size: 25px;
    font-weight: 300;
    line-height: 32px;
  }
  .contact-list__item {
    display: flex;
    justify-content: center;
    align-items: center;
    gap: 8px;
  }
  .contact-list__icon {
    width: 24px;
    height: 24px;
    fill: var(--rose);
  }
  .service-line {
    position: absolute;
    left: 0;
    right: 0;
    top: 352px;
    font-size: 21px;
    font-weight: 400;
    letter-spacing: 4px;
    text-transform: uppercase;
  }
</style>
</head>
<body>
<main class="canvas">
  <section class="card card--front" aria-label="Card front">
    <div class="brand-mark">
      <div class="brand-mark__circle"></div>
      <p class="brand-mark__name">Tessa Marwick</p>
    </div>
  </section>

  <section class="card card--back" aria-label="Card back">
    <div class="contact-block">
      <h1 class="contact-block__name">Tessa Marwick</h1>
      <p class="contact-block__title">Finance Specialist</p>
      <ul class="contact-list">
        <li class="contact-list__item">
          <svg class="contact-list__icon" viewBox="0 0 24 24" aria-hidden="true">
            <path d="M6.6 10.8a15.1 15.1 0 0 0 6.6 6.6l2.2-2.2a1 1 0 0 1 1-.25 11.4 11.4 0 0 0 3.6.57 1 1 0 0 1 1 1V20a1 1 0 0 1-1 1A17 17 0 0 1 3 4a1 1 0 0 1 1-1h3.5a1 1 0 0 1 1 1c0 1.25.2 2.45.57 3.6a1 1 0 0 1-.25 1z"/>
          </svg>
          <span>0438 217 905</span>
        </li>
        <li class="contact-list__item">
          <svg class="contact-list__icon" viewBox="0 0 24 24" aria-hidden="true">
            <path d="M2 5h20v14H2z M2 5l10 8 10-8" fill="none" stroke="#b56b74" stroke-width="0"/>
            <path d="M2 5h20v1.2l-10 7.6L2 6.2z"/>
            <path d="M2 8.2l10 7.6 10-7.6V19H2z"/>
          </svg>
          <span>tessa@marwickfinance.com.au</span>
        </li>
      </ul>
    </div>
    <p class="service-line">Residential / Commercial / Equipment</p>
  </section>
</main>
</body>
</html>
```